Campaign Flyer for a local election

Black and white election flyer

See information below to be included:

Re-elect Morton
Experienced Glenmoor Board Member
Experienced NYC Principal
Experienced leader

One Year Board Accomplishments:
-Installed New Park Lights (Bollards)
-Red Brick Road Repair Project
-Established Closer Ties with Our local precinct to frequently monitor the community with directed security patrols. Requested an increased police presence.
-Met with the 82nd Precinct Officials & Assemblywoman, Linda Marwick to discuss our security issues
- Focused on maintenance of streetlights to make brighter streets
-Negotiated Contract & Hired Our New Landscaper, Hollowfield Landscapers
-Major Homeowner Shrub Replacement Project
- Addressing Standing Water in our Park (Installed French Drain)
- Replaced and upgraded all 5 outdoor circuit breaker panels
-Write monthly community newsletters
-Sewer cleaning project (had all community catch basins cleaned)
-Carefully overseeing our new school project. Coordinating with the sponsor and the school directors
-Delivered a very healthy budget to the community
-Works closely with our committees
-Events: Zoo event, Petting Zoo, Outdoor Movie Night, Egg Hunt

It is my intent to seek re-election.
(Photo) Morton Velasquez
-Dedicated to improving our community
-Hard-working…He gets thing done!
-Trustworthy

. .

Please note, I am submitting new information under accomplishments. The list of accomplishments should be in the same sequence, starting with: Met with the 82nd Precinct....
Please carefully review.
----------------------------------------------------------------------------------------------------------------------------------------------------------------

Re-elect Morton
Experienced NYC Principal
Experienced leader

Last Year’s Board Accomplishments:

-Met with the 82nd Precinct Officials & Assemblywoman, Linda Marwick, to discuss our security issues. Requested increased police presence.
-Established a strong partnership with the 82nd precinct to frequently monitor the community with directed security patrols.
-Replaced all new park lights (Bollards) to make the park brighter
- Focused on maintenance of streetlights to make streets brighter
-‘Fixing Our Streets Project’ (Repaired all cracked/missing red bricks)
-Homeowner Shrub Replacement Project (Replaced hundreds of bushes)
- I write the monthly community newsletter
-Carefully overseeing our new school project. Coordinating with the sponsor and the school director
-Monitoring C of O’s and homeowners Insurance

(Photo) Morton Velasquez
-Hard-working! I get things done!
-Trustworthy

. .

Re-elect Morton
Experienced NYC Principal
Experienced leader

(Photo) Morton Velasquez
-Trustworthy

. .

Target Market(s)

A Community electing a Board Member

Industry/Entity Type

residential election

Requirements
Must have
• all black, white and grey print. Flyers will not be printed in color
Nice to have
• See the information in the attachment below containing all my accomplishments
Should not have
• color

```html
<!DOCTYPE html>
<html lang="en">
<head>
<meta charset="utf-8">
<title>Re-elect Morton Velasquez</title>
<link rel="stylesheet" href="https://fonts.googleapis.com/css2?family=Source+Sans+3:wght@400;600;700&display=swap">
<style>
  :root {
    --ink: #141414;
    --bar: #231f20;
    --paper: #ffffff;
    --mist: #e6e7e8;
    --photo-grey: #6b6b6b;
  }
  * { margin: 0; padding: 0; box-sizing: border-box; }
  html, body { width: 848px; height: 1200px; overflow: hidden; background: var(--paper); }
  body { font-family: "Source Sans 3", "Myriad Pro", sans-serif; color: var(--ink); }
  .flyer { position: relative; width: 848px; height: 1200px; overflow: hidden; background: var(--paper); }
  .hero-shapes { position: absolute; left: 0; top: 0; width: 848px; height: 480px; }
  .name-tag {
    position: absolute; left: 23px; top: 30px; white-space: nowrap;
    color: var(--paper); font-weight: 700; font-size: 30px; line-height: 38px; letter-spacing: 4px;
  }
  .name-tag .last { display: block; padding-left: 33px; }
  .headline {
    position: absolute; left: 14px; top: 196px; width: 236px;
    font-weight: 700; font-size: 44px; line-height: 46px; letter-spacing: 3px;
    white-space: nowrap;
    padding-bottom: 6px; border-bottom: 1.5px solid var(--ink);
  }
  .headline .line { display: block; }
  .credentials {
    position: absolute; left: 14px; top: 306px;
    list-style: none; font-size: 18px; line-height: 24px; white-space: nowrap;
  }
  .section-band {
    position: absolute; left: 0; width: 848px; height: 52px;
    background: var(--ink); color: var(--paper);
    font-weight: 400; font-size: 34px; line-height: 52px; padding-left: 34px; letter-spacing: -0.3px;
    white-space: nowrap;
  }
  .band-accomplishments { top: 489px; }
  .band-intent { top: 1016px; }
  .accomplishments {
    position: absolute; left: 34px; top: 561px; width: 772px;
    list-style: none; font-size: 17.6px; line-height: 24px; letter-spacing: 0.1px;
  }
  .qualities-panel { position: absolute; left: 0; top: 1068px; width: 848px; height: 132px; background: var(--mist); }
  .qualities {
    position: absolute; left: 34px; top: 10px;
    list-style: none; font-size: 17.6px; line-height: 24px; letter-spacing: 0.1px;
  }
  .accomplishments li::before, .qualities li::before { content: "- "; }
</style>
</head>
<body>
<main class="flyer">
  <svg class="hero-shapes" viewBox="0 0 848 480">
    <path d="M0,156 H248 L374,434 H0 Z" fill="var(--mist)"/>
    <rect x="0" y="434" width="376" height="11" fill="var(--bar)"/>
    <path role="img" aria-label="Portrait photograph of Morton Velasquez"
          d="M188,0 H848 V476 H462 Q418,476 392,440 Z" fill="var(--photo-grey)"/>
    <path d="M0,24 H254 Q266,24 271,34 L306,106 Q309,118 296,118 H0 Z" fill="var(--ink)"/>
  </svg>

  <h1 class="name-tag">MORTON<span class="last">VELASQUEZ</span></h1>

  <h2 class="headline"><span class="line">RE-ELECT</span><span class="line">MORTON</span></h2>
  <ul class="credentials">
    <li>Experienced Glenmoor Board Member</li>
    <li>Experienced NYC Principal</li>
    <li>Experienced leader</li>
  </ul>

  <h2 class="section-band band-accomplishments">ONE YEAR BOARD ACCOMPLISHMENTS :</h2>
  <ul class="accomplishments">
    <li>Installed New Park Lights (Bollards)</li>
    <li>Red Brick Road Repair Project</li>
    <li>Established Closer Ties with Our local precinct to frequently monitor the community with directed security patrols. Requested an increased police presence.</li>
    <li>Met with the 82nd Precinct Officials &amp; Assemblywoman, Linda Marwick to discuss our security issues</li>
    <li>Focused on maintenance of streetlights to make brighter streets</li>
    <li>Negotiated Contract &amp; Hired Our New Landscaper, Hollowfield Landscapers</li>
    <li>Major Homeowner Shrub Replacement Project</li>
    <li>Addressing Standing Water in our Park (Installed French Drain)</li>
    <li>Replaced and upgraded all 5 outdoor circuit breaker panels</li>
    <li>Write monthly community newsletters</li>
    <li>Sewer cleaning project (had all community catch basins cleaned)</li>
    <li>Carefully overseeing our new school project. Coordinating with the sponsor and the school directors</li>
    <li>Delivered a very healthy budget to the community</li>
    <li>Works closely with our committees</li>
    <li>Events: Zoo event, Petting Zoo, Outdoor Movie Night, Egg Hunt</li>
  </ul>

  <h2 class="section-band band-intent">IT IS MY INTENT TO SEEK RE-ELECTION</h2>
  <section class="qualities-panel">
    <ul class="qualities">
      <li>Dedicated to improving our community</li>
      <li>Hard-working…He gets thing done!</li>
      <li>Trustworthy</li>
    </ul>
  </section>
</main>
</body>
</html>
```